Modifications to a letterhead design

The following changes are being made to show other options for staff. Thanks

Part A - Letterhead
I have the two letterheads that I need a slight change made. I have already turned them into templates. So I hope the changes to the design can still occur.
Where the school name is, could you remove the yellow line and brown shape. Instead, please write:

Brell Creek Lakeside High School

The colour is to be in the chocolate brown colour. The font size and positioning for the school name can stay the same.

Changes to occur for colour and black&white

Part B - Certificates

Principal Award:
- Where the school name is, could you remove the yellow line and brown shape. Instead, please write: Brell Creek Lakeside High School
The colour is to be in the chocolate brown colour. The font size remains the same and it needs to be centred on the page
- Please remove the purple box and have no box
- for the 5 award categories please have not dot before the word, and centre the 5 categories and ensure the first letter is in capitals but the rest of the letters are lower case, for example: School Service
- Please remove the principal banner and change to ribbon on page 2 of the slide show - you will need to tidy it up or create new as I just cut and pasted it
- then could I have 2 Principal Awards - one addressing the above, and a second one addressing those things mentioned above plus removing all the colour at the bottom of the page

Year Advisor Award
- Use the same template design for the Principal Award mentioned above (including the details mentioned above). This time change the name on the ribbon (on page 2 of powerpoint) to Year Adviser's Award (only fist letter is capital , the rest lower case).
- Also, for the Year Adviser's Award, please produce 5 certificates with 1 category on each certificate e.g. School Service (again only first letter in capitals, the rest lower case). Also, the 5 certificates have a changed colour at the bottom of the page (including the 3 twirling ribbons). Colours for the bottom of the certificates are: Green, purple, red, yellow and blue.
- Please also create the 5 Year Adviser certificates without any colour at the bottom as well

```html
<!DOCTYPE html>
<html lang="en">
<head>
<meta charset="utf-8">
<title>Principal's Award Certificate</title>
<link rel="stylesheet" href="https://fonts.googleapis.com/css2?family=Arimo:wght@400;700&family=Tinos:ital,wght@0,400;0,700;1,700&display=swap">
<style>
  :root {
    --paper: #ffffff;
    --purple: #9b3f97;
    --purple-deep: #7d2a79;
    --ribbon: #5e1f3f;
    --ribbon-dark: #3d1228;
    --gold: #f2c41c;
    --chocolate: #3e2a1e;
    --ink: #111111;
    --category: #8c2b8a;
  }
  html, body { margin: 0; padding: 0; overflow: hidden; background: var(--paper); }
  .certificate {
    position: relative;
    width: 849px;
    height: 1200px;
    overflow: hidden;
    background: var(--paper);
    font-family: "Arimo", Arial, sans-serif;
    color: var(--ink);
  }
  .top-swoosh { position: absolute; left: 0; top: 0; }
  .school-banner { position: absolute; left: 560px; top: 0; }
  .school-mark {
    position: absolute;
    left: 565px; top: 160px; width: 130px;
    display: flex; flex-direction: column; align-items: center; gap: 8px;
    text-align: center;
  }
  .school-mark .mark-circle {
    width: 56px; height: 56px; border-radius: 50%;
    background: var(--gold);
  }
  .school-mark .mark-name {
    font-family: "Tinos", "Times New Roman", serif;
    font-weight: 700; font-size: 14px; line-height: 1.15;
    color: var(--paper);
  }
  .school-name {
    position: absolute; left: 93px; top: 176px;
    margin: 0;
    font-family: "Tinos", "Times New Roman", serif;
    font-weight: 400; font-size: 32px;
    color: var(--chocolate);
    white-space: nowrap;
  }
  .motto {
    position: absolute; left: 142px; top: 222px;
    margin: 0;
    font-family: "Tinos", "Times New Roman", serif;
    font-style: italic; font-weight: 700; font-size: 16px;
    color: var(--ink);
  }
  .award-ribbon { position: absolute; left: 122px; top: 330px; }
  .award-label {
    position: absolute; left: 0; right: 0; top: 441px;
    margin: 0; text-align: center; font-size: 27px;
  }
  .achievements-label {
    position: absolute; left: 0; right: 0; top: 643px;
    margin: 0; text-align: center; font-size: 27px;
  }
  .categories {
    position: absolute; left: 0; right: 0; top: 700px;
    margin: 0; padding: 0; list-style: none; text-align: center;
    font-family: "Tinos", "Times New Roman", serif;
    font-weight: 700; font-size: 36px; line-height: 53px;
    color: var(--category);
  }
</style>
</head>
<body>
<main class="certificate">
  <svg class="top-swoosh" width="849" height="130" viewBox="0 0 849 130" aria-hidden="true">
    <path d="M0 0 H849 V20 C700 40 560 30 430 48 C300 64 160 62 0 95 Z" fill="var(--purple)"/>
    <path d="M0 95 C160 62 300 64 430 48 C560 30 700 40 849 20 V30 C700 50 560 42 430 58 C300 74 160 74 0 105 Z" fill="var(--gold)"/>
    <path d="M0 112 C160 82 300 80 430 66 C560 52 700 58 849 40 V46 C700 64 560 60 430 72 C300 86 160 90 0 118 Z" fill="var(--ribbon-dark)"/>
  </svg>

  <svg class="school-banner" width="140" height="315" viewBox="0 0 140 315" aria-hidden="true">
    <path d="M0 0 H140 V312 L70 292 L0 312 Z" fill="var(--purple)"/>
    <path d="M0 0 H140 V8 H0 Z" fill="var(--purple-deep)"/>
  </svg>
  <div class="school-mark">
    <span class="mark-circle"></span>
    <span class="mark-name">Brell Creek Lakeside High School</span>
  </div>

  <h1 class="school-name">Brell Creek Lakeside High School</h1>
  <p class="motto">“For so much, what shall we repay?”</p>

  <svg class="award-ribbon" width="340" height="80" viewBox="0 0 340 80" role="img" aria-label="Principal's Award">
    <path d="M0 22 L32 17 L32 66 L0 71 L14 46 Z" fill="var(--ribbon-dark)"/>
    <path d="M340 22 L308 17 L308 66 L340 71 L326 46 Z" fill="var(--ribbon-dark)"/>
    <path d="M22 14 C110 1 230 1 318 14 L318 62 C230 49 110 49 22 62 Z" fill="var(--ribbon)"/>
    <text x="170" y="47" text-anchor="middle" font-family="Arimo, Arial, sans-serif" font-weight="700" font-size="23" fill="#ffffff" letter-spacing="1">PRINCIPAL’S AWARD</text>
  </svg>

  <p class="award-label">Awarded to:</p>
  <p class="achievements-label">for the following achievments:</p>

  <ul class="categories">
    <li>School Service</li>
    <li>Community Service</li>
    <li>Sporting Achievement</li>
    <li>Leadership</li>
    <li>Academic Achievement</li>
  </ul>
</main>
</body>
</html>
```